Business Card Design

Electrical Contracting buisness
need a buisness card relating to that buisness

Reason: Just need to discuss with partner

Industry/Entity Type

Business

Contact Information for Business Card

Dale Fenwick Electrical
0431 756 918
dalefenwick7@mailnest.example
REC 58714

```html
<!DOCTYPE html>
<html lang="en">
<head>
<meta charset="utf-8">
<title>Dale Fenwick Electrical – Business Card</title>
<link rel="stylesheet" href="https://fonts.googleapis.com/css2?family=Lora:wght@400&display=swap">
<style>
  :root {
    --backdrop: #2b2b2d;
    --card-light: #f4f4f6;
    --card-mid: #dcdde2;
    --photo-dark: #2a1518;
    --photo-red: #b3233a;
    --photo-blue: #5fa9d4;
    --ink: #2e2e33;
    --ink-soft: #55565c;
  }
  html, body {
    margin: 0;
    padding: 0;
    width: 1200px;
    height: 900px;
    overflow: hidden;
    background: var(--backdrop);
  }
  .card {
    position: absolute;
    left: 120px;
    top: 156px;
    width: 960px;
    height: 588px;
    overflow: hidden;
    background: var(--card-light);
    box-shadow: 0 20px 50px rgba(0,0,0,0.45);
  }
  .card-art {
    position: absolute;
    inset: 0;
    width: 960px;
    height: 588px;
  }
  .brand {
    position: absolute;
    left: 420px;
    top: 96px;
    width: 520px;
    text-align: center;
    font-family: "Lora", serif;
    color: var(--ink);
  }
  .brand-name {
    margin: 0;
    font-size: 42px;
    font-weight: 400;
    letter-spacing: 0.5px;
  }
  .brand-licence {
    margin: 6px 0 0;
    font-size: 15px;
    color: var(--ink-soft);
    letter-spacing: 0.5px;
  }
  .contact {
    position: absolute;
    left: 590px;
    top: 390px;
    margin: 0;
    padding: 0;
    list-style: none;
    font-family: "Lora", serif;
    font-size: 22px;
    color: var(--ink);
  }
  .contact-item {
    display: flex;
    align-items: center;
    gap: 18px;
    margin-bottom: 10px;
  }
  .contact-icon {
    width: 22px;
    height: 22px;
    flex: none;
  }
</style>
</head>
<body>
  <article class="card">
    <svg class="card-art" viewBox="0 0 960 588" aria-hidden="false">
      <defs>
        <linearGradient id="lightGround" x1="0" y1="0" x2="1" y2="1">
          <stop offset="0" stop-color="#ffffff"/>
          <stop offset="0.6" stop-color="#ececef"/>
          <stop offset="1" stop-color="#d6d7dc"/>
        </linearGradient>
        <linearGradient id="photoGround" x1="0" y1="0" x2="1" y2="1">
          <stop offset="0" stop-color="#1d1416"/>
          <stop offset="0.45" stop-color="#7a1a2a"/>
          <stop offset="0.7" stop-color="#b3233a"/>
          <stop offset="1" stop-color="#3a1a20"/>
        </linearGradient>
      </defs>
      <rect class="cable-backdrop" x="0" y="0" width="960" height="588" fill="url(#lightGround)"
            role="img" aria-label="Faint photo of bundled electrical cables"/>
      <path class="cable-photo" d="M0 0 H330 C 470 120 560 360 585 588 H0 Z" fill="url(#photoGround)"
            role="img" aria-label="Photo of stripped electrical and data cables against red light streaks"/>
    </svg>

    <header class="brand">
      <h1 class="brand-name">Dale Fenwick Electrical</h1>
      <p class="brand-licence">REC 58714</p>
    </header>

    <ul class="contact">
      <li class="contact-item">
        <svg class="contact-icon" viewBox="0 0 24 24" aria-hidden="true">
          <rect x="2" y="5" width="20" height="14" fill="var(--ink)"/>
          <path d="M2 5 L12 13 L22 5" fill="none" stroke="#f4f4f6" stroke-width="1.6"/>
        </svg>
        <span>dalefenwick7@mailnest.example</span>
      </li>
      <li class="contact-item">
        <svg class="contact-icon" viewBox="0 0 24 24" aria-hidden="true">
          <path d="M3 9 C3 5 21 5 21 9 L17 10 L16 8 H8 L7 10 Z" fill="var(--ink)"/>
          <rect x="6" y="11" width="12" height="9" rx="1.5" fill="var(--ink)"/>
        </svg>
        <span>0431 756 918</span>
      </li>
    </ul>
  </article>
</body>
</html>
```